Indie musician needs album cover art

I am an independant musician releasing my second album via digital sources. I plan to make it available on Vendly and other digital stores but primarily distribute it free through Tunegrove.

The album's music style is a blend of singer-songwriter folk, punk, alt country, electronic rock and spoken word. The lyrical content is a dark journey through travel in foreign countries, relationships, airports and theatres, formed during my own journey as an audio engineer for a travelling theatre show.

The album is called "Ash Under Glass" - at times both a plea and a directive. I would like the album cover to reflect a sense of longing, restlessness, unease and movement. A subversive tone is also possible.

I have had a go at designing a couple of ideas myself, using my own photos. I like the ideas but I am not skilled in graphic design and am unable to take them further to get the right feel and look. I will post these as examples of tone. The finished work does not need to copy either of these.

A .zip of the album can be downloaded here (low fi mp3):

http://fylo.io/Qx7rT4

Target Market(s)

People who enjoy thoughtful, honest, homemade music. Definitely not a teeny pop audience. Adult, subversive, educated, emotional...

Industry/Entity Type

Graphic Design

Requirements
Must have
• Artist name (no caps): kipwren
Album name (prefer no caps): ash under glass

```html
<!DOCTYPE html>
<html lang="en">
<head>
<meta charset="utf-8">
<title>kipwren – ash under glass</title>
<link rel="stylesheet" href="https://fonts.googleapis.com/css2?family=Bodoni+Moda:ital,wght@1,400&display=swap">
<style>
  :root {
    --page: #ffffff;
    --sky-blue: #3b4796;
    --dusk-violet: #7a6aa8;
    --haze: #f6efe6;
    --ember-red: #b3311f;
    --deep-red: #9c2418;
    --photo-pink: #d889a8;
    --photo-gold: #e9c98a;
    --photo-violet: #8e6aa6;
    --title-ink: #ffffff;
  }
  html, body {
    margin: 0;
    width: 1200px;
    height: 900px;
    overflow: hidden;
    background: var(--page);
  }
  .stage {
    position: relative;
    width: 1200px;
    height: 900px;
  }
  .cover {
    position: absolute;
    top: 191px;
    width: 532px;
    height: 531px;
    overflow: hidden;
    background:
      radial-gradient(ellipse 260px 170px at 0% 50%, rgba(255,250,240,0.95), rgba(255,250,240,0) 100%),
      linear-gradient(180deg, var(--sky-blue) 0%, var(--dusk-violet) 32%, #c9b3c4 52%, #d98a7a 70%, var(--ember-red) 88%, var(--deep-red) 100%);
  }
  .cover--front { left: 43px; }
  .cover--back { left: 615px; transform: rotate(180deg); }
  .cover__photo {
    position: absolute;
    left: 12px;
    top: 10px;
    width: 510px;
    height: 510px;
    border-radius: 50%;
    background:
      radial-gradient(circle at 10% 50%, rgba(255,248,230,0.95) 0%, rgba(255,248,230,0) 45%),
      radial-gradient(circle at 55% 40%, var(--photo-pink) 0%, rgba(216,137,168,0) 40%),
      radial-gradient(circle at 60% 72%, var(--photo-gold) 0%, rgba(233,201,138,0) 35%),
      linear-gradient(180deg, #5a4a8e 0%, var(--photo-violet) 35%, #caa2b6 60%, #c9613f 85%, #a8382a 100%);
    opacity: 0.92;
  }
  .cover__title {
    position: absolute;
    margin: 0;
    font-family: "Bodoni Moda", "Didot", serif;
    font-style: italic;
    font-weight: 400;
    color: var(--title-ink);
    white-space: nowrap;
    line-height: 1;
  }
  .cover__album {
    left: 24px;
    top: 15px;
    font-size: 19px;
    transform: rotate(180deg);
  }
  .cover__artist {
    left: 24px;
    top: 52px;
    font-size: 66px;
  }
</style>
</head>
<body>
  <main class="stage">
    <section class="cover cover--front">
      <div class="cover__photo" role="img" aria-label="Night photograph of a festival crowd with balloons and strings of lights, seen through a circular frame"></div>
      <p class="cover__title cover__album">ash under glass</p>
      <h1 class="cover__title cover__artist">kipwren</h1>
    </section>
    <section class="cover cover--back">
      <div class="cover__photo" role="img" aria-label="Night photograph of a festival crowd with balloons and strings of lights, seen through a circular frame, turned upside down"></div>
      <p class="cover__title cover__album">ash under glass</p>
      <h2 class="cover__title cover__artist">kipwren</h2>
    </section>
  </main>
</body>
</html>
```